Book Cover for a Short Story called “Salt Orchard"

Pretty Straightforward. Looking for a 5.5X8.5 book cover. The story is a very short (40 pages) story about a man who moves from Greece to Canada in 1920. I have three photos to provide. One is the house that he left in greece. THen I have photos of him and his wife who he met in Toronto. I think I want the house photo on the front...
I will need cover for paper back and e-book. The ISBN numbers are:

ISBN: 978-1-2459083-3-2 (e-book)
ISBN: 978-1-2459083-1-7 (paperback)

If you want you can read it at https://kelvarunde.com/fiction/salt-orchard/

Colors
0094D4
00A9DD
6FCCEA
C7EBF8
E9F6FB

Requirements
Must have
• Room for a blurb about the book on the back cover. ISBN Number

```html
<!DOCTYPE html>
<html lang="en">
<head>
<meta charset="utf-8">
<title>Salt Orchard — Cover Wrap</title>
<link href="https://fonts.googleapis.com/css2?family=EB+Garamond:wght@400;500&family=Sacramento&display=swap" rel="stylesheet">
<style>
  :root {
    --backdrop: #4b4b4b;
    --paper: #ffffff;
    --ink: #0d0d0d;
    --body-ink: #1c1c1c;
    --gold: #b8954f;
    --photo-light: #e4e2de;
    --photo-mid: #a9a6a0;
    --photo-dark: #6d6a66;
    --suit: #2c3c5c;
  }
  html, body {
    margin: 0;
    padding: 0;
    width: 1200px;
    height: 761px;
    overflow: hidden;
    background: var(--backdrop);
  }
  .canvas {
    position: relative;
    width: 1200px;
    height: 761px;
  }
  .cover-wrap {
    position: absolute;
    left: 146px;
    top: 30px;
    width: 1432px;
    height: 1104px;
    background: var(--paper);
    transform: scale(0.634);
    transform-origin: top left;
    font-family: "EB Garamond", Georgia, serif;
    color: var(--ink);
  }
  /* Back cover */
  .back-title {
    position: absolute;
    left: 78px;
    top: 100px;
    margin: 0;
    font-weight: 400;
    font-size: 118px;
    line-height: 1;
    white-space: nowrap;
  }
  .back-title .title-script {
    font-family: "Sacramento", cursive;
    color: var(--gold);
    font-size: 96px;
    margin-left: 10px;
  }
  .blurb {
    position: absolute;
    margin: 0;
    font-size: 19.5px;
    line-height: 22.8px;
    text-align: justify;
    color: var(--body-ink);
  }
  .blurb-main {
    left: 73px;
    top: 258px;
    width: 582px;
  }
  .blurb-side {
    left: 328px;
    top: 538px;
    width: 326px;
  }
  .author-portrait {
    position: absolute;
    left: 15px;
    top: 495px;
    width: 380px;
    height: 478px;
    background:
      radial-gradient(ellipse 30% 22% at 48% 22%, #d9b29a 0%, #d9b29a 60%, transparent 100%),
      radial-gradient(ellipse 60% 55% at 45% 72%, var(--suit) 0%, var(--suit) 55%, rgba(44,60,92,0) 100%);
  }
  .isbn {
    position: absolute;
    left: 50px;
    top: 1010px;
    margin: 0;
    font-size: 17px;
  }
  /* Front cover */
  .front-title {
    position: absolute;
    left: 775px;
    top: 80px;
    width: 600px;
    height: 280px;
    margin: 0;
    font-weight: 400;
  }
  .front-title .title-serif {
    position: absolute;
    left: 130px;
    top: 0;
    font-size: 180px;
    line-height: 1;
  }
  .front-title .title-script {
    position: absolute;
    left: 200px;
    top: 150px;
    font-family: "Sacramento", cursive;
    color: var(--gold);
    font-size: 120px;
    line-height: 1;
  }
  .photo-collage {
    position: absolute;
    left: 783px;
    top: 375px;
    width: 600px;
    height: 565px;
    background: linear-gradient(160deg, var(--photo-light) 0%, var(--photo-mid) 55%, var(--photo-dark) 100%);
    border-radius: 6px;
  }
  .author-name {
    position: absolute;
    left: 775px;
    width: 600px;
    top: 990px;
    margin: 0;
    text-align: center;
    font-size: 36px;
    font-weight: 400;
    letter-spacing: 8px;
    text-transform: uppercase;
  }
</style>
</head>
<body>
<main class="canvas">
  <section class="cover-wrap">
    <!-- Back cover -->
    <h2 class="back-title">Salt<span class="title-script">orchard</span></h2>
    <p class="blurb blurb-main">Lorem ipsum dolor sit amet, consectetur adipiscing elit, sed do eiusmod tempor incididunt ut labore et dolore magna aliqua. Quis ipsum suspendisse ultrices gravida. Risus commodo viverra maecenas accumsan lacus vel facilisis. Lorem ipsum dolor sit amet, consectetur adipiscing elit, sed do eiusmod tempor incididunt ut labore et dolore magna aliqua.<br>Quis ipsum suspendisse ultrices gravida. Risus commodo viverra maecenas accumsan lacus vel facilisis. Lorem ipsum dolor sit amet, consectetur adipiscing elit, sed do eiusmod tempor incididunt ut labore et dolore magna aliqua. Quis ipsum suspendisse ultrices gravida. Risus commodo viverra maecenas accumsan lacus vel facilisis.</p>
    <div class="author-portrait" role="img" aria-label="Portrait of the author in a navy blazer with arms crossed"></div>
    <p class="blurb blurb-side">Quis ipsum suspendisse ultrices gravida. Risus commodo viverra maecenas accumsan lacus vel facilisis. Lorem ipsum dolor sit amet, consectetur adipiscing elit, sed do eiusmod tempor incididunt ut labore et dolore magna aliqua. Quis ipsum suspendisse ultrices gravida. Risus commodo viverra maecenas accumsan lacus vel facilisis.</p>
    <p class="isbn">ISBN: 978-1-2459083-1-7</p>

    <!-- Front cover -->
    <h1 class="front-title">
      <span class="title-serif">Salt</span>
      <span class="title-script">orchard</span>
    </h1>
    <div class="photo-collage" role="img" aria-label="Stack of old black-and-white photographs: a stone house in Greece, a young woman and a young man"></div>
    <p class="author-name">Kelvar Unde</p>
  </section>
</main>
</body>
</html>
```